Business Card Design - Cryotherapy

We need a custom created business card for our company FrostLeaf Spa. We provide whole body cryotherapy and localized cryotherapy to our clients. Please be creative.
Please see our website for idea's on design.
www.frostleafspa-example.com
Industry/Entity Type
Business
Contact Information for Business Card
Name, Position, Phone Number, Address, Website, Email
Look and feel
Each slider illustrates characteristics of the customer's brand and the style your logo design should communicate.

```html
<!DOCTYPE html>
<html lang="en">
<head>
<meta charset="utf-8">
<title>FrostLeaf Spa — Business Card</title>
<link href="https://fonts.googleapis.com/css2?family=Arimo:wght@400;700&display=swap" rel="stylesheet">
<style>
  :root {
    --backdrop: #4a4340;
    --card: #1c1c1d;
    --card-edge: #2a2a2b;
    --green: #1f9a5a;
    --teal: #1aa6b3;
    --ink: #e9e9e9;
    --rule: #8a8a8a;
  }
  * { box-sizing: border-box; margin: 0; padding: 0; }
  html, body {
    width: 1200px; height: 787px; overflow: hidden;
    background: var(--backdrop);
    font-family: "Arimo", Arial, sans-serif;
  }
  .stage {
    position: relative; width: 1200px; height: 787px;
  }
  .card {
    position: absolute; width: 525px; height: 300px;
    background: var(--card);
    border: 1px solid var(--card-edge);
    box-shadow: 0 10px 30px rgba(0,0,0,.35);
  }
  .card--front { left: 45px; top: 244px; }
  .card--back { left: 630px; top: 244px; }

  .front-mark {
    position: absolute; inset: 0;
    display: flex; align-items: center; justify-content: center; gap: 14px;
  }
  .mark-dot {
    width: 18px; height: 18px; border-radius: 50%; background: var(--teal);
  }
  .brand-name {
    font-size: 34px; font-weight: 400; color: var(--teal); letter-spacing: 1px;
  }

  .back-brand {
    position: absolute; right: 34px; top: 34px;
    display: flex; align-items: center; gap: 10px;
  }
  .back-brand .brand-name { font-size: 28px; }
  .back-brand .mark-dot { width: 14px; height: 14px; }

  .person {
    position: absolute; left: 30px; top: 88px;
  }
  .person-name { font-size: 17px; color: var(--green); }
  .person-role { font-size: 13px; color: var(--teal); margin-top: 5px; }
  .role-rule {
    position: absolute; left: 80px; right: 34px; top: 128px;
    height: 1px; background: var(--rule);
  }
  .contacts {
    position: absolute; left: 30px; top: 138px; list-style: none;
  }
  .contacts li {
    display: flex; align-items: center; gap: 8px;
    font-size: 13.5px; color: var(--ink); line-height: 22px;
  }
  .contacts svg { width: 12px; height: 12px; fill: var(--green); flex: none; }
  .address-rule {
    position: absolute; left: 30px; right: 34px; top: 210px;
    height: 1px; background: var(--rule);
  }
  .address {
    position: absolute; right: 34px; top: 220px;
    text-align: right; font-size: 14px; line-height: 17px; color: var(--ink);
    font-style: normal;
  }
</style>
</head>
<body>
<main class="stage">
  <section class="card card--front" aria-label="Card front">
    <div class="front-mark">
      <span class="mark-dot"></span>
      <span class="brand-name">FrostLeaf Spa</span>
    </div>
  </section>

  <section class="card card--back" aria-label="Card back">
    <div class="back-brand">
      <span class="mark-dot"></span>
      <span class="brand-name">FrostLeaf Spa</span>
    </div>

    <div class="person">
      <p class="person-name">Daniel Varek, RN,BSN</p>
      <p class="person-role">Owner</p>
    </div>
    <div class="role-rule"></div>

    <ul class="contacts">
      <li>
        <svg viewBox="0 0 12 12"><path d="M2.5 0.8l2 2.2-1.1 1.3c.6 1.5 1.8 2.7 3.3 3.3l1.3-1.1 2.2 2-1.2 2.4C4.9 10.6 1.4 7.1.4 2.3z"/></svg>
        (555) 014-2739
      </li>
      <li>
        <svg viewBox="0 0 12 12"><path d="M0 2h12v1.2L6 7 0 3.2zM0 4.6l6 3.8 6-3.8V10H0z"/></svg>
        info@frostleafspa-example.com
      </li>
      <li>
        <svg viewBox="0 0 12 12"><circle cx="6" cy="6" r="6"/><path d="M1 6h10M6 1c-2 2.8-2 7.2 0 10M6 1c2 2.8 2 7.2 0 10" stroke="#1c1c1d" stroke-width=".8" fill="none"/></svg>
        www.frostleafspa-example.com
      </li>
    </ul>

    <div class="address-rule"></div>
    <address class="address">
      2710 Lakeview Road<br>
      Suite 240<br>
      Maple Grove, IL 60099
    </address>
  </section>
</main>
</body>
</html>
```